Strata Edge Supply Business Card Design Challenge

Please create me a simple card using my logo. I'm not looking for anything abstract.
A couple of colours for text and maybe something on the card so the whole card isn't just a white board.
Please send me samples and I'll reply with suggestions to refine the design. Thank you

Reason: The Ormeau address was incorrect in the brief, so I have updated that so the 4 and 5 star submissions can be updated and resubmitted please!!! Sorry and thank you

Target Market(s)

Mining companies and rock producing aggregate companies. Quarries

Industry/Entity Type

Mining

Contact Information for Business Card

Name - Lewis Trenholm / Company Logo AND Strata Edge Supply Pty Ltd / position - Managing Director / address1 - Unit 3, 14 Kestrel Parade, Ormeau 4208 Queensland AU / address2 - PO Box 917, Tallis Ridge 4318 Queensland AU / mobile - 0427 195 864 / phone - 07 5571 9346 / fax - 07 5571 9420 / email - lt@strataedgesupply.example.com.au / website - www.strataedgesupply.example.com.au

Requirements
Must have
• Business details as per the above. The phone and fax numbers will be confirmed before the end of the project. Thank you
• SINGLE SIDED ONLY please on Card, not transparent plastic

```html
<!DOCTYPE html>
<html lang="en">
<head>
<meta charset="utf-8">
<title>Strata Edge Supply – Business Card</title>
<link rel="stylesheet" href="https://fonts.googleapis.com/css2?family=Montserrat:wght@600;800&family=Source+Sans+3:wght@400&display=swap">
<style>
  :root {
    --backdrop: #a5a2a2;
    --card: #f7f7f7;
    --slate: #4d5359;
    --blue: #1aa0dc;
    --ink: #4a4f55;
    --white: #ffffff;
  }
  html, body {
    margin: 0;
    width: 1200px;
    height: 883px;
    overflow: hidden;
    background: var(--backdrop);
  }
  .card {
    position: absolute;
    left: 243px;
    top: 226px;
    width: 712px;
    height: 430px;
    border-radius: 22px;
    overflow: hidden;
    background: var(--card);
    font-family: "Source Sans 3", "Source Sans Pro", sans-serif;
    color: var(--ink);
  }
  .card__waves {
    position: absolute;
    inset: 0;
    width: 712px;
    height: 430px;
  }
  .holder {
    position: absolute;
    right: 27px;
    top: 45px;
    text-align: right;
    color: var(--white);
  }
  .holder__name {
    font-family: "Montserrat", sans-serif;
    font-weight: 600;
    font-size: 25px;
    letter-spacing: 0.4px;
    margin: 0;
    line-height: 1.2;
  }
  .holder__role {
    font-size: 16px;
    margin: 8px 0 0;
  }
  .company {
    position: absolute;
    left: 38px;
    top: 180px;
    width: 290px;
    margin: 0;
    font-family: "Montserrat", sans-serif;
    font-weight: 800;
    font-size: 36px;
    line-height: 1.1;
    color: var(--slate);
    text-transform: uppercase;
  }
  .contact {
    position: absolute;
    top: 293px;
    margin: 0;
    padding: 0;
    list-style: none;
    font-size: 17px;
    line-height: 26.5px;
  }
  .contact--left { left: 40px; }
  .contact--right { left: 401px; }
  .contact li {
    display: flex;
    align-items: center;
    white-space: nowrap;
  }
  .contact .icon {
    width: 15px;
    height: 15px;
    fill: var(--blue);
    flex: none;
    margin-right: 14px;
  }
  .contact .icon--inline { margin-left: 8px; margin-right: 6px; }
  .contact .indent { padding-left: 29px; }
  .web__domain { color: var(--blue); }
</style>
</head>
<body>
<main class="card">
  <svg class="card__waves" viewBox="0 0 712 430" aria-hidden="true">
    <path fill="var(--slate)" d="M0,0 H712 V190 C620,178 570,90 400,44 C260,10 110,14 0,28 Z"/>
    <path fill="var(--blue)" d="M0,40 C120,18 270,20 390,54 C560,100 610,180 712,192 V200 C600,190 550,110 380,66 C250,34 110,40 0,58 Z"/>
    <path fill="var(--blue)" d="M60,64 C200,40 330,44 420,74 C330,56 200,52 60,64 Z"/>
  </svg>

  <header class="holder">
    <h1 class="holder__name">Lewis Trenholm</h1>
    <p class="holder__role">Managing Director</p>
  </header>

  <h2 class="company">Strata Edge Supply</h2>

  <ul class="contact contact--left">
    <li>
      <svg class="icon" viewBox="0 0 16 16"><path d="M4 0h8a1.5 1.5 0 0 1 1.5 1.5v13A1.5 1.5 0 0 1 12 16H4a1.5 1.5 0 0 1-1.5-1.5v-13A1.5 1.5 0 0 1 4 0zm0 2v10h8V2zm4 11a1 1 0 1 0 0 2 1 1 0 0 0 0-2z"/></svg>
      0427 195 864
    </li>
    <li>
      <svg class="icon" viewBox="0 0 16 16"><path d="M1 5c0-2 3-3 7-3s7 1 7 3v1h-4V4.5H5V6H1zm3 2h8l2 7H2zm4 2a2 2 0 1 0 0 4 2 2 0 0 0 0-4z"/></svg>
      07 5571 9346
      <svg class="icon icon--inline" viewBox="0 0 16 16"><path d="M4 0h8v5H4zM1 6h14v7h-3v3H4v-3H1zm4 5v3h6v-3z"/></svg>
      07 5571 9420
    </li>
    <li>
      <svg class="icon" viewBox="0 0 16 16"><path d="M0 3h16v1L8 9 0 4zm0 3 8 5 8-5v7H0z"/></svg>
      lt@strataedgesupply.example.com.au
    </li>
    <li>
      <svg class="icon" viewBox="0 0 16 16"><path d="M8 0a8 8 0 1 0 0 16A8 8 0 0 0 8 0zm-1 1.2C5.8 2.6 5.1 4.6 5 7H1.1A7 7 0 0 1 7 1.2zm2 0A7 7 0 0 1 14.9 7H11c-.1-2.4-.8-4.4-2-5.8zM6 7c.1-2.3.9-4.2 2-5.3 1.1 1.1 1.9 3 2 5.3zm-4.9 2H5c.1 2.4.8 4.4 2 5.8A7 7 0 0 1 1.1 9zM6 9h4c-.1 2.3-.9 4.2-2 5.3C6.9 13.2 6.1 11.3 6 9zm5 0h3.9A7 7 0 0 1 9 14.8c1.2-1.4 1.9-3.4 2-5.8z"/></svg>
      <span>www.<span class="web__domain">strataedgesupply.example</span>.com.au</span>
    </li>
  </ul>

  <ul class="contact contact--right">
    <li>
      <svg class="icon" viewBox="0 0 16 16"><path d="M8 0a5.5 5.5 0 0 1 5.5 5.5C13.5 10 8 16 8 16S2.5 10 2.5 5.5A5.5 5.5 0 0 1 8 0zm0 3a2.5 2.5 0 1 0 0 5 2.5 2.5 0 0 0 0-5z"/></svg>
      Unit 3, 14 Kestrel Parade,
    </li>
    <li class="indent">Marlow Creek 4311 Queensland AU</li>
    <li>
      <svg class="icon" viewBox="0 0 16 16"><path d="M3 3h8a4 4 0 0 1 4 4v4H1V5a2 2 0 0 1 2-2zm3 0v1h4V0h3v2h-2v2zm1 8h2v5H7z"/></svg>
      PO Box 917, Tallis Ridge 4318
    </li>
    <li class="indent">Queensland AU</li>
  </ul>
</main>
</body>
</html>
```